Business Card Design Project : Tidewell Press

In preparation for market launch, Whistler's Tidewell Press require the development of a business card. Tidewell Press is a Community online publishing web portal. We provide the the city of Whistler located in B.C. (Canada) business directories, News, Classified ads, News, Events and blogs etc.

The main focus of the brand is to help local businesses to corporate with their online advertisement and marketing. Meeting our clients face to face is a must (B2B).

Target Market(s)

The target market is B2B customers. Business Owners to Marketing, advertising Managers

Industry/Entity Type

Business

Requirements
Must have
• - The business card will be two sided.
the BACK side will have our logo which consist of (icon, url,slogan) submited. The logo will be middle and centred.

The FRONT side should have company details:

Company Legal Name: FERNDALE TIDEWELL PRESS

Owen Marsk
Director of Sales & Marketing

www.ferndaletidewell.biz
owen@ferndaletidewell.biz

Phone: 555 014 3826
#2817 - 562 E. Harlow Ave.
Vancouver, B.C. K7P2R4 Canada
Nice to have
• - For the "FRONT" side of our business card. You can separate or re-arrange with our logo components (icon, logo,slogan). It does not have to be together.

Also our company legal name is rather long so arrange or organize the name in a way to make it shorter. Your experience and creativity will have to come in play.
Should not have
• should not have other colors beside logo color and black text (2 colors). Also nothing Three dimensional

```html
<!DOCTYPE html>
<html lang="en">
<head>
<meta charset="utf-8">
<title>Tidewell Press — Business Card</title>
<link rel="stylesheet" href="https://fonts.googleapis.com/css2?family=Open+Sans:wght@400;600;700&display=swap">
<style>
  :root {
    --brand-blue: #1b6cb3;
    --ink: #231f20;
    --paper: #ffffff;
    --backdrop: #e6e7e9;
    --muted: #3a3a3a;
  }
  * { box-sizing: border-box; margin: 0; padding: 0; }
  html, body {
    width: 1200px;
    height: 944px;
    overflow: hidden;
    background: var(--backdrop);
    font-family: "Open Sans", sans-serif;
    color: var(--ink);
  }
  .sheet {
    position: relative;
    width: 1200px;
    height: 944px;
  }
  .card {
    position: absolute;
    left: 250px;
    width: 700px;
    height: 400px;
    background: var(--paper);
    border-radius: 26px;
    overflow: hidden;
  }
  .card--back { top: 48px; }
  .card--front { top: 496px; }

  /* Back side: brand block centred */
  .brand-block {
    position: absolute;
    inset: 0;
    display: flex;
    flex-direction: column;
    align-items: center;
    justify-content: center;
    gap: 10px;
  }
  .brand-name {
    display: flex;
    align-items: center;
    gap: 16px;
    font-size: 52px;
    font-weight: 700;
    color: var(--brand-blue);
    line-height: 1;
    margin-bottom: 14px;
  }
  .brand-dot {
    width: 40px;
    height: 40px;
    border-radius: 50%;
    background: var(--brand-blue);
  }
  .brand-url {
    font-size: 38px;
    font-weight: 700;
    color: var(--ink);
    line-height: 1.1;
  }
  .brand-slogan {
    font-size: 30px;
    font-weight: 400;
    color: var(--brand-blue);
    line-height: 1.1;
  }

  /* Front side */
  .front-brand {
    position: absolute;
    left: 48px;
    top: 52px;
    display: flex;
    align-items: center;
    gap: 12px;
    font-size: 34px;
    font-weight: 700;
    color: var(--brand-blue);
    line-height: 1;
  }
  .front-brand .brand-dot { width: 28px; height: 28px; }
  .front-slogan {
    position: absolute;
    right: 40px;
    top: 88px;
    font-size: 22px;
    color: var(--ink);
  }
  .person {
    position: absolute;
    left: 48px;
    top: 168px;
  }
  .person-name {
    font-size: 25px;
    font-weight: 400;
    color: var(--brand-blue);
    line-height: 1.2;
  }
  .person-title {
    font-size: 16px;
    color: var(--ink);
    margin-top: 4px;
  }
  .contact {
    position: absolute;
    left: 366px;
    top: 160px;
    list-style: none;
    font-size: 17.5px;
    line-height: 1.45;
    color: var(--ink);
  }
  .contact li {
    display: flex;
    align-items: flex-start;
    gap: 10px;
  }
  .contact li + li { margin-top: 4px; }
  .contact-icon {
    flex: 0 0 16px;
    width: 16px;
    height: 16px;
    margin-top: 4px;
    fill: var(--brand-blue);
  }
  .footer-band {
    position: absolute;
    left: 0;
    bottom: 0;
    width: 700px;
    height: 120px;
  }
  .footer-url {
    position: absolute;
    left: 0;
    right: 0;
    bottom: 22px;
    text-align: center;
    font-size: 24px;
    letter-spacing: 2px;
    color: var(--paper);
  }
</style>
</head>
<body>
<main class="sheet">

  <section class="card card--back" aria-label="Business card, back side">
    <div class="brand-block">
      <div class="brand-name"><span class="brand-dot" aria-hidden="true"></span>Tidewell Press</div>
      <div class="brand-url">www.ferndaletidewell.biz</div>
      <div class="brand-slogan">Your information gateway</div>
    </div>
  </section>

  <section class="card card--front" aria-label="Business card, front side">
    <div class="front-brand"><span class="brand-dot" aria-hidden="true"></span>Tidewell Press</div>
    <p class="front-slogan">Your information gateway</p>

    <div class="person">
      <p class="person-name">Owen Marsk</p>
      <p class="person-title">Director of Sales &amp; Marketing</p>
    </div>

    <ul class="contact">
      <li>
        <svg class="contact-icon" viewBox="0 0 16 16" aria-hidden="true"><path d="M8 1 L15 8 H13 V15 H9.5 V10.5 H6.5 V15 H3 V8 H1 Z"/></svg>
        <span>#2817 - 562 E. Harlow Ave.<br>Vancouver, B.C. K7P2R4 Canada</span>
      </li>
      <li>
        <svg class="contact-icon" viewBox="0 0 16 16" aria-hidden="true"><path d="M4 1 C2 2 1 4 2 7 C3.5 11 6 13.5 10 15 C12 15.5 14 14 15 12 L12 9.5 L10 11 C8 10 6 8 5 6 L6.5 4 Z"/></svg>
        <span>555 014 3826</span>
      </li>
      <li>
        <svg class="contact-icon" viewBox="0 0 16 16" aria-hidden="true"><path d="M1 4 H15 V13 H1 Z M1 4 L8 9.5 L15 4" fill="none" stroke="#1b6cb3" stroke-width="1.8" stroke-linejoin="round"/></svg>
        <span>owen@ferndaletidewell.biz</span>
      </li>
    </ul>

    <svg class="footer-band" viewBox="0 0 700 120" preserveAspectRatio="none" aria-hidden="true">
      <path d="M0 22 C 220 46, 470 46, 700 10 L700 120 L0 120 Z" fill="var(--brand-blue)"/>
      <path d="M0 34 C 220 58, 470 58, 700 24 L700 120 L0 120 Z" fill="var(--ink)"/>
    </svg>
    <p class="footer-url">www.ferndaletidewell.biz</p>
  </section>

</main>
</body>
</html>
```